Human Resource Consultant's Website needs an Updated Look

I'm an HR Consultant based in Denver that caters to small business owners. I like my logo, and the existing content (though open to editorial suggestions) but would like to reformat my site and possibly update graphics. I want to be able to manage content moving forward. TLMWAdvisory.com

Target Market(s)

Small business owners with 10-500 employees in Metro Denver

Coding

Coded - Design and coding required

Font styles to use
Other font styles liked:
• Closer to existing font but open to suggestions

Colors

Designer to choose colors to be used in the design.

Requirements
Must have
• Links on landing page to other pages
• Visual appeal to younger demographic found in the small to medium sized business owner
• Scroll down rather than use the clunky "ladder" tabs I see now
• Color palate that compliments logo
Nice to have
• Pages that scroll down, links to page content on the first page,
Should not have
• Hate the standard employee-employer photos on most HR websites. Would prefer to use illustrations over the typical photos

```html
<!DOCTYPE html>
<html lang="en">
<head>
<meta charset="utf-8">
<title>TLMW ~ HR Advisory</title>
<link rel="stylesheet" href="https://fonts.googleapis.com/css2?family=Montserrat:wght@400;500;600;700&display=swap">
<style>
:root{
  --blue:#0f6ea6;
  --blue-dark:#1a4f8a;
  --teal:#0a93c0;
  --green:#9cc31b;
  --ink:#1f2a33;
  --muted:#8a8f94;
  --panel:#f3f3f3;
  --white:#ffffff;
}
*{box-sizing:border-box;margin:0;padding:0}
html,body{width:1200px;height:2990px;overflow:hidden}
body{position:relative;font-family:"Montserrat",sans-serif;color:var(--ink);background:var(--white)}
.abs{position:absolute}
a{color:inherit}

/* header */
.site-header{position:absolute;left:0;top:0;width:1200px;height:100px;background:var(--white)}
.brand{left:156px;top:22px;display:flex;align-items:center;gap:14px}
.brand-mark{width:52px;height:52px;border-radius:50%;background:var(--blue)}
.brand-name{font-size:26px;font-weight:700;color:var(--blue-dark);line-height:1}
.brand-tag{font-size:10px;color:var(--green);margin-top:6px;font-weight:500}
.callbar{right:200px;top:22px;font-size:13px;font-weight:600;color:var(--green);display:flex;align-items:center;gap:8px}
.callbar strong{color:var(--blue-dark);font-size:15px}
.social{display:flex;gap:8px}
.social span{width:24px;height:24px;border-radius:50%;border:2px solid var(--green)}
.social span.on{background:var(--green)}
.main-nav{left:570px;top:64px;display:flex;gap:34px;font-size:13px;font-weight:600}
.main-nav .active{color:var(--green)}

/* hero */
.hero{left:0;top:100px;width:1200px;height:525px;background:linear-gradient(180deg,#5b6066 0%,#707478 55%,#8c6a4c 78%,#6b4d34 100%)}
.hero-art{right:140px;top:50px;width:460px;height:420px;background:linear-gradient(135deg,#3aa6e0,#e3c41c 40%,#e8583a 65%,#2fa84f);opacity:.75;border-radius:6px}
.hero-title{left:156px;top:272px;font-size:24px;font-weight:700;color:var(--white);line-height:1.3;width:420px}
.hero-text{left:156px;top:358px;font-size:13px;color:#eef;line-height:1.5;width:380px}
.btn-solid{left:156px;top:416px;width:128px;height:32px;background:var(--green);color:var(--white);font-size:11px;font-weight:600;display:flex;align-items:center;justify-content:center}
.round-arrow{width:32px;height:32px;border-radius:50%;display:flex;align-items:center;justify-content:center}

/* approach */
.eyebrow{font-size:13px;font-weight:700;color:var(--blue-dark)}
.eyebrow.green{color:var(--green)}
.heading{font-size:25px;font-weight:500;line-height:1.22}
.approach-copy{left:612px;top:738px;width:340px;font-size:12px;color:var(--muted);line-height:1.65}
.btn-outline{width:128px;height:32px;border:1.5px solid var(--green);color:var(--green);font-size:11px;font-weight:600;display:flex;align-items:center;justify-content:center}
.approach-art{left:436px;top:868px;width:534px;height:288px;background:linear-gradient(135deg,#3a3a3e,#6c6c70 60%,#2c2c30)}
.quote-box{left:232px;top:966px;width:368px;height:232px;background:linear-gradient(135deg,var(--blue-dark),var(--teal));color:var(--white);padding:56px 48px;font-size:15px;line-height:1.6}

/* services */
.center{left:0;width:1200px;text-align:center}
.service{display:flex;flex-direction:column;align-items:center;justify-content:center;gap:18px;font-size:13px;font-weight:700;text-align:center;background:var(--panel)}
.service.featured{background:linear-gradient(135deg,var(--blue-dark),var(--teal));color:var(--white)}

/* publications */
.pub-band{left:0;top:1774px;width:970px;height:398px;background:var(--panel)}
.pub-art{left:600px;top:1710px;width:446px;height:338px;background:linear-gradient(135deg,#dfe5ea,#9eb3c4 55%,#c8d3dc)}
.pub-name{color:var(--green);font-weight:700}
.pub-link{left:156px;top:1990px;width:360px;font-size:14px;line-height:1.4;text-decoration:underline}

/* blog */
.post{background:var(--panel)}
.post-art{width:280px;height:160px}
.post-title{position:absolute;left:22px;top:20px;width:240px;font-size:14px;font-weight:700;line-height:1.35}
.post-title.link{color:var(--blue-dark);text-decoration:underline}
.post-date{position:absolute;left:22px;top:96px;font-size:13px;color:var(--blue-dark)}
.post-date.green{color:var(--green)}

/* footer */
.site-footer{left:0;top:2668px;width:1200px;height:322px;background:linear-gradient(90deg,var(--blue-dark),var(--teal));color:var(--white)}
.f-head{font-size:14px;font-weight:700;color:var(--green)}
.f-text{font-size:12px;line-height:1.7}
.newsletter{left:460px;top:140px;width:282px;height:32px;background:var(--white);display:flex;align-items:center;justify-content:space-between;padding:0 12px;font-size:11px;color:var(--muted)}
.f-rule{left:156px;top:252px;width:914px;height:1px;background:rgba(255,255,255,.35)}
</style>
</head>
<body>

<header class="site-header">
  <div class="abs brand">
    <span class="brand-mark"></span>
    <div>
      <div class="brand-name">TLMW ~ HR Advisory</div>
      <div class="brand-tag">Building HR Competencies in Business Leaders</div>
    </div>
  </div>
  <div class="abs callbar">Call Us:
    <svg width="14" height="20" viewBox="0 0 14 20"><rect x="1" y="1" width="12" height="18" rx="2" fill="none" stroke="#9cc31b" stroke-width="2"/></svg>
    <strong>123-456-7890</strong>
    <div class="social"><span></span><span class="on"></span><span></span></div>
  </div>
  <nav class="abs main-nav">
    <a class="active">Home</a><a>My Approach</a><a>My Services</a><a>Dana</a><a>Contact Me</a>
  </nav>
</header>

<section class="abs hero">
  <div class="abs hero-art" role="img" aria-label="Stacked colourful clay blocks each marked with a person figure"></div>
</section>
<h1 class="abs hero-title">Human capital is the wealth an organization possesses,</h1>
<p class="abs hero-text">Derived from its people, which is critical to its economic success.</p>
<a class="abs btn-solid">Explore More</a>
<span class="abs round-arrow" style="left:50px;top:348px;border:1.5px solid #fff">
  <svg width="14" height="10" viewBox="0 0 14 10"><path d="M13 5H2M5 1L1 5l4 4" fill="none" stroke="#fff" stroke-width="1.6"/></svg></span>
<span class="abs round-arrow" style="left:1118px;top:348px;background:var(--blue)">
  <svg width="14" height="10" viewBox="0 0 14 10"><path d="M1 5h11M9 1l4 4-4 4" fill="none" stroke="#fff" stroke-width="1.6"/></svg></span>

<section>
  <div class="abs eyebrow" style="left:232px;top:702px">My Approach</div>
  <h2 class="abs heading" style="left:232px;top:738px;width:330px">Entrepreneurs<br>are innovative risk-taking business leaders.</h2>
  <div class="abs eyebrow green" style="left:612px;top:702px">Build Your Human Resources Competencies!</div>
  <p class="abs approach-copy">I consult with small to medium sized business owners to support, complement or develop their skill set in talent management. My human resources consulting services focus on ...</p>
  <a class="abs btn-outline" style="left:232px;top:868px">Explore More</a>
  <div class="abs approach-art" role="img" aria-label="Pins joined by red thread forming a network on dark felt"></div>
  <p class="abs quote-box">You had an idea and ran with it! But when you looked back, were your employees following? If not, partner with me to…</p>
</section>

<section>
  <div class="abs center eyebrow" style="top:1276px">My Services</div>
  <h2 class="abs center heading" style="top:1310px">I consult with small to medium sized<br>business owners to support!</h2>

  <div class="abs service" style="left:156px;top:1414px;width:280px;height:200px">
    <svg width="52" height="46" viewBox="0 0 52 46" fill="none" stroke="#0f6ea6" stroke-width="2"><circle cx="26" cy="9" r="6"/><circle cx="10" cy="16" r="5"/><circle cx="42" cy="16" r="5"/><rect x="6" y="26" width="40" height="6"/><path d="M10 32v12M42 32v12M26 32v12"/></svg>
    <span>Hr &amp; Business<br>Consultant</span>
  </div>
  <div class="abs service featured" style="left:460px;top:1396px;width:280px;height:234px">
    <svg width="52" height="48" viewBox="0 0 52 48" fill="none" stroke="#fff" stroke-width="2"><circle cx="16" cy="9" r="6"/><path d="M6 46V22h20v24M16 30v16"/><path d="M34 8h8M34 24h8M34 40h8M38 8v32M26 24h8"/><circle cx="46" cy="8" r="3"/><circle cx="46" cy="24" r="3"/><circle cx="46" cy="40" r="3"/></svg>
    <span>Hr Project<br>Manager</span>
    <span class="round-arrow" style="width:26px;height:26px;border:1.5px solid #fff">
      <svg width="12" height="9" viewBox="0 0 14 10"><path d="M1 5h11M9 1l4 4-4 4" fill="none" stroke="#fff" stroke-width="1.8"/></svg></span>
  </div>
  <div class="abs service" style="left:764px;top:1414px;width:280px;height:200px">
    <svg width="52" height="48" viewBox="0 0 52 48" fill="none" stroke="#0f6ea6" stroke-width="2"><rect x="18" y="2" width="32" height="24"/><circle cx="10" cy="12" r="6"/><path d="M2 46V24h16v22M18 28l10-8"/><path d="M24 20v-6M32 20v-10M40 20v-8"/></svg>
    <span>Trainer &amp;<br>Facilitator</span>
  </div>
</section>

<section>
  <div class="abs pub-band"></div>
  <div class="abs pub-art" role="img" aria-label="Digital network of connected people icons around a globe"></div>
  <div class="abs eyebrow" style="left:156px;top:1834px">Publications</div>
  <h2 class="abs heading" style="left:156px;top:1870px;width:340px">Publications<br>and featuring by <span class="pub-name">Dana Whitlow</span></h2>
  <a class="abs pub-link">Guild of People Managers: Workaholics: Job ‘Addicts’ Can Hurt Selves, Morale, Company</a>
  <span class="abs round-arrow" style="left:156px;top:2072px;width:26px;height:26px;border:1.5px solid var(--blue)">
    <svg width="12" height="9" viewBox="0 0 14 10"><path d="M13 5H2M5 1L1 5l4 4" fill="none" stroke="#0f6ea6" stroke-width="1.8"/></svg></span>
  <span class="abs round-arrow" style="left:188px;top:2072px;width:26px;height:26px;background:var(--blue)">
    <svg width="12" height="9" viewBox="0 0 14 10"><path d="M1 5h11M9 1l4 4-4 4" fill="none" stroke="#fff" stroke-width="1.8"/></svg></span>
</section>

<section>
  <div class="abs center eyebrow" style="top:2252px">Latest Blog</div>
  <article class="abs post" style="left:156px;top:2300px;width:280px;height:290px">
    <div class="post-art" role="img" aria-label="Hands holding seedlings growing from coin stacks" style="background:linear-gradient(135deg,#2c3a1c,#8a7a4a 50%,#3a3020)"></div>
    <div style="position:relative">
      <h3 class="post-title">Benefits and Beyond…..</h3>
      <div class="post-date">October 1, 2016</div>
    </div>
  </article>
  <article class="abs post" style="left:460px;top:2300px;width:280px;height:290px">
    <div class="post-art" role="img" aria-label="Rising stacks of coins beside a coin jar" style="background:linear-gradient(135deg,#e2e2e0,#b3aea4 60%,#d6d4cf)"></div>
    <div style="position:relative">
      <h3 class="post-title link">Beyond Comp and Benefits….</h3>
      <div class="post-date green">September 2, 2016</div>
    </div>
  </article>
  <article class="abs post" style="left:764px;top:2300px;width:280px;height:290px">
    <div class="post-art" role="img" aria-label="Hand holding a tablet with cloud technology icons" style="background:linear-gradient(135deg,#1c1c1e,#4a4a4e 55%,#2a2a2c)"></div>
    <div style="position:relative">
      <h3 class="post-title">Organizational Culture – How to Improve or Enhance Its Current State</h3>
      <div class="post-date">August 1, 2016</div>
    </div>
  </article>
</section>

<footer class="abs site-footer">
  <div class="abs f-head" style="left:156px;top:70px">Contact Info</div>
  <div class="abs f-text" style="left:156px;top:94px;width:280px">
    <strong style="font-size:14px">Call Us: 720.555.0148</strong><br>
    E. DWhitlow@TLMWAdvisory.com<br>
    <strong style="display:block;margin-top:14px">Dana Whitlow ~ HR Advisory, LLC</strong>
    Suite 410, 1550 Larimer St,<br>Denver, CO - 80202
  </div>
  <div class="abs f-head" style="left:460px;top:70px">Newsletter Sign up</div>
  <p class="abs f-text" style="left:460px;top:96px;width:290px">Sign up for our newsletter to see our news and achievements</p>
  <div class="abs newsletter">Enter your email
    <svg width="16" height="14" viewBox="0 0 16 14"><path d="M1 1l14 6-14 6 3-6z" fill="#0f6ea6"/></svg></div>
  <div class="abs f-head" style="left:842px;top:70px">Quick Link</div>
  <ul class="abs f-text" style="left:842px;top:96px;list-style:none">
    <li>Home</li><li>My Approach</li><li>My Services</li><li>Dana</li><li>Contact Me</li>
  </ul>
  <span class="abs round-arrow" style="left:1122px;top:66px;width:26px;height:26px;background:var(--green)">
    <svg width="12" height="8" viewBox="0 0 12 8"><path d="M1 7l5-5 5 5" fill="none" stroke="#1a4f8a" stroke-width="2"/></svg></span>
  <div class="abs f-rule"></div>
  <div class="abs" style="left:156px;top:282px;font-size:11px">© 2018 Dana Whitlow ~ HR Advisory, LLC. All Right Reserved</div>
  <div class="abs" style="left:842px;top:276px;display:flex;align-items:center;gap:10px;font-size:13px;font-weight:700;color:var(--green)">Get Social:
    <div class="social"><span></span><span class="on"></span><span></span></div>
  </div>
</footer>

</body>
</html>
```